Brightwell Giving Inc

We need a full re-design of our non-profit organization website (www.brightwellgiving.org). Ideally, we are looking to make it more attractive, user-friendly, and interactive with our business model.

Please make sure to user colors that ago with our logo.

We need a homepage done and we also need a content page done where we will use for the other pages to fill with content.

Target Market(s)

Clothes/textiles donations.

Industry/Entity Type

Charity

Number of Pages Required

2 page

Colors

Designer to choose colors to be used in the design.

Requirements
Must have
• It must match the styling of our logo and same colors as current website. (www.brightwellgiving.org)
Nice to have
• Sleek homepage that is easy to understand and get our main points across.

```html
<!DOCTYPE html>
<html lang="en">
<head>
<meta charset="utf-8">
<title>Brightwell Giving Inc</title>
<link rel="stylesheet" href="https://fonts.googleapis.com/css2?family=Raleway:wght@400;500;600;700&family=Roboto:wght@700&display=swap">
<style>
:root{
  --green:#2f9673;
  --green-dark:#247a5d;
  --ink:#141414;
  --panel:#1b1b1b;
  --white:#ffffff;
  --grey-text:#444444;
  --logo-text:#1f5a2a;
}
*{margin:0;padding:0;box-sizing:border-box}
html,body{width:759px;height:1200px;overflow:hidden;background:var(--white)}
body{font-family:"Raleway",sans-serif;position:relative}
.page{position:relative;width:759px;height:1200px;overflow:hidden}

.site-header{position:absolute;left:0;top:0;width:759px;height:47px;background:var(--green)}
.nav{position:absolute;top:19px;display:flex;gap:9px;font-size:7.5px;font-weight:700;color:var(--white)}
.nav-left{left:95px}
.nav-right{left:507px}
.nav a{color:var(--white);text-decoration:none;position:relative}
.nav a.active{color:#1f3f33}
.nav a.active::after{content:"";position:absolute;left:0;top:11px;width:11px;height:2px;background:#1f3f33}
.brand-tab{position:absolute;left:292px;top:0;width:176px;height:47px;background:var(--white);border-radius:0 0 8px 8px;display:flex;align-items:center;justify-content:center;gap:6px}
.brand-mark{width:14px;height:14px;background:var(--green);border-radius:2px}
.brand-name{font-size:11px;font-weight:700;color:var(--logo-text);letter-spacing:.2px}

.hero{position:absolute;left:0;top:47px;width:759px;height:311px;background:linear-gradient(90deg,#0f2a33 0%,#173a44 45%,#2a3f45 100%)}
.hero-photo{position:absolute;right:0;top:0;width:381px;height:311px;background:radial-gradient(ellipse at 50% 55%,#c89b86 0%,#8a6a5e 35%,#2a2f33 75%,#1a2a30 100%)}
.hero-title{position:absolute;left:95px;top:129px;font-family:"Roboto",sans-serif;font-weight:700;font-size:22px;line-height:37px;color:var(--white)}
.btn-outline{display:flex;align-items:center;justify-content:center;border:2px solid var(--green);border-radius:3px;color:var(--white);font-weight:600;text-decoration:none}
.hero .btn-outline{position:absolute;left:96px;top:213px;width:118px;height:33px;font-size:14px;background:rgba(0,0,0,.15)}

.mission{position:absolute;left:0;top:358px;width:759px;height:95px;background:var(--ink);text-align:center}
.scroll-cue{position:absolute;left:361px;top:-9px;width:38px;height:28px;border-radius:0 0 19px 19px;background:#1e2f37}
.mission p{position:absolute;left:0;top:31px;width:759px;font-size:10px;font-weight:600;color:var(--white);line-height:19px}

.tiles{position:absolute;left:0;top:453px;width:759px;display:grid;grid-template-columns:repeat(4,1fr);grid-auto-rows:237px}
.tile{position:relative;text-align:center}
.tile-dark{background:var(--panel);color:var(--white)}
.tile-light{background:var(--white);color:var(--grey-text)}
.tile-rule{position:absolute;left:62px;top:41px;width:52px;height:4px}
.tile-dark .tile-rule{background:var(--white)}
.tile-light .tile-rule{background:var(--ink)}
.tile-text{position:absolute;left:18px;right:18px;top:72px;font-size:9.5px;line-height:19px}
.tile .btn-outline{position:absolute;left:52px;top:184px;width:88px;height:24px;font-size:10px;font-weight:500}
.tile-light .btn-outline{color:var(--ink)}
.photo-a{background:linear-gradient(160deg,#5a5a5a,#2a2a2a 60%,#888)}
.photo-b{background:linear-gradient(180deg,#3a3a3a,#9a9a9a 45%,#4a4a4a)}
.photo-c{background:linear-gradient(170deg,#1e1e1e,#6e6e6e 50%,#2a2a2a)}
.photo-d{background:linear-gradient(135deg,#3a2a1e,#8a6040 45%,#c08a4a 75%,#5a3a20)}

.finder{position:absolute;left:0;top:927px;width:759px;height:113px}
.finder h2{position:absolute;left:0;width:759px;top:47px;text-align:center;font-size:14.5px;font-weight:500;color:var(--ink)}
.zip-row{position:absolute;left:292px;top:72px;display:flex;align-items:center;gap:4px;font-size:11px;color:var(--ink)}
.zip-input{width:90px;height:16px;border:2px solid var(--green);border-radius:3px}
.zip-btn{margin-left:2px;width:55px;height:16px;background:var(--green);color:var(--white);border-radius:3px;font-size:8px;display:flex;align-items:center;justify-content:center}

.site-footer{position:absolute;left:0;top:1040px;width:759px;height:160px;background:#161616;color:var(--white)}
.site-footer .brand-tab{top:0}
.footer-heading{position:absolute;top:52px;font-size:14px;font-weight:600;color:var(--green)}
.contact{position:absolute;left:96px;top:74px;font-size:7px;line-height:9px}
.contact-line{display:flex;gap:4px;align-items:flex-start;margin-bottom:5px}
.socials{position:absolute;left:324px;top:63px;display:flex;gap:10px}
.socials span{width:20px;height:20px;border-radius:50%;background:#5a5a5a}
.site-footer .btn-outline{position:absolute;left:321px;top:95px;width:117px;height:32px;font-size:14px}
.copyright{position:absolute;left:0;width:759px;top:143px;text-align:center;font-size:7px}
.links{position:absolute;left:534px;top:74px;display:grid;grid-template-columns:61px 60px;row-gap:3px;font-size:7px;font-weight:700}
</style>
</head>
<body>
<div class="page">
  <header class="site-header">
    <nav class="nav nav-left"><a class="active">Home</a><a>Missions</a><a>How it works</a><a>About Us</a></nav>
    <div class="brand-tab"><span class="brand-mark"></span><span class="brand-name">BRIGHTWELL GIVING</span></div>
    <nav class="nav nav-right"><a>Sponsors</a><a>News</a><a>Donate</a><a>Wall of needs</a></nav>
  </header>

  <section class="hero">
    <div class="hero-photo" role="img" aria-label="Close-up portrait of a curly-haired young child"></div>
    <h1 class="hero-title">Think globaly<br>While donating locally</h1>
    <a class="btn-outline">Donate</a>
  </section>

  <section class="mission">
    <div class="scroll-cue">
      <svg width="38" height="28" viewBox="0 0 38 28"><polyline points="13,10 19,16 25,10" fill="none" stroke="#fff" stroke-width="2"/></svg>
    </div>
    <p>WE ARE AN OPEN BOOK ORGANIZATION<br>OUR GOAL IS TO BE WITH AND WITHIN THE COMMUNITY</p>
  </section>

  <section class="tiles">
    <div class="tile photo-a" role="img" aria-label="Black and white portrait of a young boy"></div>
    <div class="tile tile-dark"><span class="tile-rule"></span><p class="tile-text">We are a family based non-profit organization in the name of Brightwell Giving Inc</p><a class="btn-outline">Learn More</a></div>
    <div class="tile photo-b" role="img" aria-label="Black and white portrait of a smiling older woman"></div>
    <div class="tile tile-light"><span class="tile-rule"></span><p class="tile-text">we have personally donated over $50,000 dollars to various foundation and organization who are already helping local communities.</p><a class="btn-outline">Learn More</a></div>
    <div class="tile tile-light"><span class="tile-rule"></span><p class="tile-text">As we have therefore opportunity, let us do good unto all men, especially unto them who are of the household of faith.</p><a class="btn-outline">Learn More</a></div>
    <div class="tile photo-c" role="img" aria-label="Black and white portrait of an elderly bearded man in a knit cap"></div>
    <div class="tile tile-dark"><span class="tile-rule"></span><p class="tile-text">Brightwell Giving has been a dedicated member of its local communities over the past four years</p><a class="btn-outline">Learn More</a></div>
    <div class="tile photo-d" role="img" aria-label="Mother hugging her young son outdoors"></div>
  </section>

  <section class="finder">
    <h2>Find Local Donation Place</h2>
    <div class="zip-row"><span>Zip:</span><span class="zip-input"></span><span class="zip-btn">search</span></div>
  </section>

  <footer class="site-footer">
    <div class="brand-tab"><span class="brand-mark"></span><span class="brand-name">BRIGHTWELL GIVING</span></div>
    <h3 class="footer-heading" style="left:96px">Get In Touch</h3>
    <div class="contact">
      <div class="contact-line">
        <svg width="8" height="11" viewBox="0 0 8 11"><path d="M4 0a4 4 0 0 1 4 4c0 3-4 7-4 7S0 7 0 4a4 4 0 0 1 4-4z" fill="#2f9673"/><circle cx="4" cy="4" r="1.5" fill="#161616"/></svg>
        <span>New York Office<br>42 Harbor Lane Oakdale NY 11769</span>
      </div>
      <div class="contact-line">
        <svg width="9" height="9" viewBox="0 0 9 9"><path d="M1 0h2l1 2-1 1c.6 1.3 1.7 2.4 3 3l1-1 2 1v2c0 .6-.4 1-1 1C3.7 9 0 5.3 0 1c0-.6.4-1 1-1z" fill="#2f9673"/></svg>
        <span>(555) 010-4821</span>
      </div>
    </div>
    <div class="socials"><span></span><span></span><span></span><span></span></div>
    <a class="btn-outline">Donate</a>
    <h3 class="footer-heading" style="left:534px">Useful links</h3>
    <nav class="links"><span>Home</span><span>Sponsars</span><span>Missions</span><span>News</span><span>How It Works</span><span>Donate</span><span>About Us</span><span>Wall of needs</span></nav>
    <p class="copyright">© 2018 Brightwell Giving. All Rights Reserved.</p>
  </footer>
</div>
</body>
</html>
```